exclusive Speakeasy Bar Web design in New Jersey USA

We are opening a speakeasy in New Jersey USA soon. we are looking for a web designer to do our web site including the coding. we a looking for a 4 to 5 page web design. the site will be mostly static. home page, contact page, menu page and a link to a 3rd party site (most likely Quob) for reservations. we are looking for this designer to do our menu deign as well. we are looking for a quick turnaround 7-10 days. i am attaching some pictures for the designers to see the concept design and the actual current pictures with our logo as well. professionally taken pictures will be provided later on. our photographer will be taking the pictures in the next week.

Industry/Entity Type

Restaurant, Bar, Speakeasy

Coding

Coded - Design and coding required

Number of Pages Required

4 page

Requirements
Must have
• home page, contact page, menu page and a link to quob.com for reservations
Nice to have
• some videos

```html
<!DOCTYPE html>
<html lang="en">
<head>
<meta charset="utf-8">
<title>Gilded Hour — Speakeasy</title>
<link rel="stylesheet" href="https://fonts.googleapis.com/css2?family=Gilda+Display&family=Lora:wght@400;600;700&display=swap">
<style>
:root{
  --ink:#2f3035;
  --ink-deep:#2b2c2a;
  --gold:#d8b15c;
  --gold-soft:#e2bd6a;
  --paper:#ffffff;
  --text-dark:#2b2b2b;
  --text-muted:#6b6b6b;
  --text-light:#e9e6df;
  --card-line:#b8914a;
}
*{box-sizing:border-box;margin:0;padding:0}
html,body{width:1200px;height:5000px;overflow:hidden}
body{position:relative;background:var(--paper);font-family:"Lora",serif;color:var(--text-dark)}
.abs{position:absolute}
.display{font-family:"Gilda Display",serif;font-weight:400}

/* header */
.site-header{left:0;top:0;width:1200px;height:122px;background:var(--ink)}
.brand{left:93px;top:40px;font-family:"Gilda Display",serif;font-size:26px;color:var(--gold);letter-spacing:1px}
.nav{left:485px;top:50px;display:flex;gap:34px;font-size:14px;color:var(--text-light)}
.nav .active{color:var(--gold);border-bottom:1px solid var(--gold);padding-bottom:4px}
.pill{border:1.5px solid var(--gold);border-radius:30px;display:flex;align-items:center;justify-content:center;font-size:14px;font-weight:600}
.header-cta{left:960px;top:42px;width:146px;height:38px;color:var(--text-light)}

/* hero */
.hero{left:0;top:122px;width:1200px;height:554px;background:linear-gradient(110deg,#4a3f2c 0%,var(--ink) 30%)}
.hero-photo{left:484px;top:122px;width:716px;height:554px;background:linear-gradient(160deg,#3a4446 0%,#2c3234 40%,#8a5a22 70%,#c78a36 100%)}
.hero-glass{left:425px;top:171px;width:344px;height:344px;background:rgba(150,140,125,.45);backdrop-filter:blur(6px)}
.hero-title{left:93px;top:240px;width:700px;font-size:58px;line-height:68px;color:var(--gold)}
.hero-cta{left:93px;top:525px;display:flex;align-items:center;gap:14px;color:#fff;font-size:18px}

/* about */
.about-block{left:0;top:820px;width:484px;height:524px;background:var(--gold)}
.about-ring{left:35px;top:855px;width:116px;height:116px;border:1.5px solid #3a3325;border-radius:50%}
.about-photo{left:93px;top:915px;width:367px;height:475px;background:linear-gradient(170deg,#3b3a35 0%,#2d5b5a 45%,#b57a36 80%,#8c6a45 100%);box-shadow:0 18px 40px rgba(0,0,0,.35)}
.about-title{left:600px;top:895px;font-size:44px;line-height:52px;color:var(--text-dark)}
.about-copy{left:600px;top:1045px;width:520px;font-size:14.5px;line-height:24px;color:var(--text-muted)}
.about-copy p+p{margin-top:24px}

/* values */
.values{left:0;top:1548px;width:1200px;height:1822px;background:var(--ink)}
.section-title{width:1200px;left:0;text-align:center;font-size:44px;color:var(--gold)}
.rule{height:1.5px;background:var(--gold)}
.values-lead{left:0;width:1200px;top:1775px;text-align:center;font-size:14.5px;line-height:24px;color:var(--text-light)}
.value-card{top:1909px;width:313px;height:326px;border:1.5px solid var(--card-line);border-radius:4px;background:linear-gradient(180deg,#3a3b3f,#2f3035);box-shadow:0 10px 30px rgba(0,0,0,.35);padding:40px 30px}
.value-icon{width:66px;height:66px;border-radius:50%;background:var(--gold);margin-bottom:36px}
.value-card h3{font-size:22px;font-weight:700;color:#fff;margin-bottom:32px}
.value-card p{font-size:14px;line-height:18px;color:#c9c5bd}

/* drinks */
.drinks-frame{left:89px;top:2393px;width:1014px;height:847px;border:1.5px solid var(--gold);outline:1px solid var(--gold);outline-offset:-8px}
.drink-art{width:92px;height:165px;background:linear-gradient(180deg,#45464b,#3a3b40);border-radius:4px}
.drink h4{font-size:22px;font-weight:700;color:#fff}
.price{display:inline-block;border:1px solid #cfcac0;color:#e9e6df;font-size:13px;padding:1px 8px;margin:10px 0 14px}
.drink p{font-size:14px;line-height:17px;color:#c9c5bd;width:240px}
.drinks-divider{left:594px;top:2610px;width:1px;height:432px;background:var(--gold)}
.explore{left:522px;top:3120px;width:146px;height:40px;color:#fff}

/* gallery */
.gallery-title{color:var(--text-dark)}
.gallery-lead{left:0;width:1200px;top:3576px;text-align:center;font-size:14.5px;line-height:24px;color:var(--text-muted)}
.shot{box-shadow:0 4px 10px rgba(0,0,0,.25)}
.tone-a{background:linear-gradient(160deg,#394447,#2a3133 50%,#c0843a)}
.tone-b{background:linear-gradient(160deg,#2c2a26,#6a4a32 55%,#b36a3a)}
.tone-c{background:linear-gradient(160deg,#4a4a4c,#2b2b2d 45%,#b78142)}
.tone-d{background:linear-gradient(180deg,#5a3c2a,#7b5a3c 50%,#2e2a26)}
.tone-e{background:linear-gradient(180deg,#2c3a3f,#3c3a35 50%,#7a4f37)}
.tone-f{background:linear-gradient(160deg,#3b4445,#6b6a62 60%,#cfc9bd)}
.tone-g{background:linear-gradient(160deg,#2a3a3e,#24585a 60%,#6b4a3a)}

.cta-title{left:0;width:1200px;top:4365px;text-align:center;font-size:44px;color:var(--text-dark)}
.cta-btn{left:522px;top:4488px;width:146px;height:40px;color:var(--text-dark)}

/* footer */
.site-footer{left:0;top:4650px;width:1200px;height:350px;background:var(--ink-deep)}
.footer-brand{left:93px;top:4800px;font-family:"Gilda Display",serif;font-size:30px;color:var(--gold)}
.footer-col{top:4712px;color:var(--text-light);font-size:14px}
.footer-col h5{font-size:15px;font-weight:700;letter-spacing:1px;margin-bottom:40px;color:#fff}
.footer-col li{list-style:none;margin-bottom:14px;display:flex;align-items:center;gap:10px}
.socials{display:flex;gap:20px;margin-top:4px}
.socials span{width:24px;height:24px;border-radius:50%;background:#f0ede6}
.footer-rule{left:54px;top:4933px;width:1092px;height:1px;background:#77746c}
.copyright{left:0;width:1200px;top:4956px;text-align:center;font-size:14px;color:var(--text-light)}
</style>
</head>
<body>

<header class="abs site-header"></header>
<div class="abs brand">Gilded Hour</div>
<nav class="abs nav"><span class="active">Home</span><span>Menu</span><span>Contact-us</span></nav>
<div class="abs pill header-cta">Reservation</div>

<section class="abs hero"></section>
<div class="abs hero-photo" role="img" aria-label="Lounge interior with mustard tufted chairs, leather banquette and a painted heron mural"></div>
<div class="abs hero-glass"></div>
<h1 class="abs hero-title display">Escape to an Era of Elegance : Your Exclusive Speakeasy Haven</h1>
<div class="abs hero-cta">Reserve a Table
  <svg width="94" height="46" viewBox="0 0 94 46"><circle cx="23" cy="23" r="22" fill="var(--gold)"/><line x1="23" y1="23" x2="90" y2="23" stroke="#fff" stroke-width="1.5"/><polyline points="82,15 90,23 82,31" fill="none" stroke="#fff" stroke-width="1.5"/></svg>
</div>

<div class="abs about-block"></div>
<div class="abs about-ring"></div>
<div class="abs about-photo" role="img" aria-label="Bar counter with teal lighting, gold stools and mustard lounge chairs"></div>
<h2 class="abs about-title display">Sip, Savor, and Socialize :<br>Unwind at Gilded Hour</h2>
<div class="abs about-copy">
  <p>At Gilded Hour, we are passionate about creating extraordinary experiences for our guests. Step into our world and discover a haven where mixology meets imagination. Our talented team of skilled bartenders are dedicated to crafting unique and innovative cocktails that will tantalize your taste buds and awaken your senses. We believe that every drink should be a work of art, carefully curated with the finest ingredients and garnished with creativity.</p>
  <p>We are more than just a place to sip and savor. It's a social hub where connections are made, and memories are forged. Our friendly and knowledgeable staff is committed to ensuring that every visit is filled with warmth, hospitality, and personalized service. We take pride in creating a welcoming environment where you can unwind, socialize, and create lifelong memories with your loved ones.</p>
</div>

<section class="abs values"></section>
<h2 class="abs section-title display" style="top:1675px">Our Values</h2>
<div class="abs rule" style="left:535px;top:1742px;width:130px"></div>
<p class="abs values-lead">We are driven by excellence, creativity, and deep passion for our craft. With commitment to hospitality,<br>we create a welcoming environment where connections are made and memories are celebrated.</p>

<article class="abs value-card" style="left:89px"><div class="value-icon"></div><h3>Authenticity</h3><p>From our curated drink selection to our unique atmosphere, we strive to create an authentic and genuine experience that reflects who we are.</p></article>
<article class="abs value-card" style="left:439px"><div class="value-icon"></div><h3>Hospitality</h3><p>We are dedicated to creating a warm and welcoming environment where everyone feels valued, appreciated, and cared for.</p></article>
<article class="abs value-card" style="left:788px"><div class="value-icon"></div><h3>Community</h3><p>We are gathering place where all friends, families, and strangers can come together to create memories and build strong relationships.</p></article>

<div class="abs drinks-frame"></div>
<h2 class="abs section-title display" style="top:2452px">Popular Drinks</h2>
<div class="abs rule" style="left:535px;top:2518px;width:130px"></div>
<div class="abs drinks-divider"></div>

<div class="abs drink-art" style="left:170px;top:2600px" role="img" aria-label="Line drawing of a martini glass"></div>
<div class="abs drink" style="left:293px;top:2626px"><h4>Martini</h4><span class="price">13 $</span><p>This paragraph is the description of drink, which later can be edited to original description of this drink.</p></div>
<div class="abs drink-art" style="left:680px;top:2600px" role="img" aria-label="Line drawing of a Moscow mule glass"></div>
<div class="abs drink" style="left:790px;top:2626px"><h4>Moscow Mule</h4><span class="price">15 $</span><p>This paragraph is the description of drink, which later can be edited to original description of this drink.</p></div>
<div class="abs drink-art" style="left:170px;top:2850px" role="img" aria-label="Line drawing of a cosmopolitan glass"></div>
<div class="abs drink" style="left:293px;top:2874px"><h4>Cosmopolitan</h4><span class="price">14 $</span><p>This paragraph is the description of drink, which later can be edited to original description of this drink.</p></div>
<div class="abs drink-art" style="left:670px;top:2850px" role="img" aria-label="Line drawing of a negroni coupe"></div>
<div class="abs drink" style="left:790px;top:2874px"><h4>Negroni</h4><span class="price">16 $</span><p>This paragraph is the description of drink, which later can be edited to original description of this drink.</p></div>
<div class="abs pill explore">Explore All</div>

<h2 class="abs section-title display gallery-title" style="top:3472px">Photo Gallery</h2>
<div class="abs rule" style="left:535px;top:3540px;width:130px"></div>
<p class="abs gallery-lead">Take a glimpse at the smiling faces of our guests, immersed in the joy and camaraderie that fills the air. From<br>live entertainment performances to private events, our photo gallery captures the essence of Gilded Hour</p>

<div class="abs shot tone-a" style="left:89px;top:3700px;width:331px;height:181px" role="img" aria-label="Lounge with mural and mustard chairs"></div>
<div class="abs shot tone-b" style="left:429px;top:3700px;width:332px;height:181px" role="img" aria-label="Bar counter under pendant lights"></div>
<div class="abs shot tone-c" style="left:771px;top:3700px;width:330px;height:181px" role="img" aria-label="Seating area with chandelier"></div>
<div class="abs shot tone-d" style="left:89px;top:3890px;width:224px;height:181px" role="img" aria-label="Back bar shelves lined with bottles"></div>
<div class="abs shot tone-e" style="left:322px;top:3890px;width:544px;height:181px" role="img" aria-label="Long bar counter with brick wall"></div>
<div class="abs shot tone-d" style="left:876px;top:3890px;width:225px;height:181px" role="img" aria-label="Bottle shelves behind the bar"></div>
<div class="abs shot tone-f" style="left:89px;top:4080px;width:331px;height:183px" role="img" aria-label="Painted heron mural with wall sconces"></div>
<div class="abs shot tone-d" style="left:429px;top:4080px;width:332px;height:183px" role="img" aria-label="Lit shelves of spirits"></div>
<div class="abs shot tone-g" style="left:771px;top:4080px;width:330px;height:183px" role="img" aria-label="Bar area with teal counter lights"></div>

<h2 class="abs cta-title display">Skip the Wait, Reserve your spot now</h2>
<div class="abs pill cta-btn">Reservation</div>

<footer class="abs site-footer"></footer>
<div class="abs footer-brand">Gilded Hour</div>
<div class="abs footer-col" style="left:503px">
  <h5>LEGAL</h5>
  <ul><li>Privacy Policy</li><li>Terms and Conditions</li></ul>
  <div class="socials"><span></span><span></span><span></span><span></span></div>
</div>
<div class="abs footer-col" style="left:738px">
  <h5>CONTACT</h5>
  <ul>
    <li><svg width="14" height="14" viewBox="0 0 14 14"><path d="M3 1 L5 1 L6 4 L4.5 5.5 Q6 8.5 8.5 9.5 L10 8 L13 9 L13 11 Q13 13 11 13 Q1 12 1 3 Q1 1 3 1Z" fill="#f0ede6"/></svg>+1 123 4567 890</li>
    <li><svg width="14" height="12" viewBox="0 0 14 12"><rect x="1" y="1" width="12" height="10" fill="none" stroke="#f0ede6" stroke-width="1.4"/><polyline points="1,1 7,6 13,1" fill="none" stroke="#f0ede6" stroke-width="1.4"/></svg>info@gildedhour.com</li>
    <li><svg width="12" height="15" viewBox="0 0 12 15"><path d="M6 14 Q1 8 1 5.5 A5 5 0 0 1 11 5.5 Q11 8 6 14Z" fill="none" stroke="#f0ede6" stroke-width="1.4"/><circle cx="6" cy="5.5" r="1.8" fill="#f0ede6"/></svg>your address goes here</li>
  </ul>
</div>
<div class="abs footer-col" style="left:986px">
  <h5>NAVIGATION</h5>
  <ul><li>Home</li><li>Menu</li><li>Contact-us</li></ul>
</div>
<div class="abs footer-rule"></div>
<p class="abs copyright">© 2023 gildedhour. All rights reserved</p>

</body>
</html>
```